Aviation Banner Ad Designs

SkyLedgerMetrics provides access to the most accurate aircraft operating cost information, to compare Piston, Turboprop and Jet aircraft.

The banners ads will be used for retargeting/remarketing - to bring visitors back to the site. The banners should remind and reinforce the key messages of what the site provides.

Target Market(s)

Private aircraft buyers including:
- Aircraft Brokers
- Charter Operators
- Corporate Flight Departments
- Aircraft Management companies
- Financial Institutions
- Aircraft Owners
- Prospective Buyers

Requirements
Must have
• A. Banner Objective
The visual and textual content of the banner should remind the viewer about the features of the site, and prompt them to return to the site.
1. Arresting visual
2. Headline
3. Single message
4. Compelling CTA
5. Logo - big enough to see
6. Standard DWR ad sizes/specs

B. Design Elements
Logo: As attached
Main Title: Calculate Jet Operating Costs
Subtitle: Compare Ownership Usage Scenarios
Call to Action Button: Compare Ownership Costs
Background: Several images supplied as options

C. Banner Sizes
Do examples as 300×250 , 728×90 , 160×600
Final sizes to also include 320×100 , 336x280 , 300x600

Finally delivery as .jpg files.

Font - use same font as on site

```html
<!DOCTYPE html>
<html lang="en">
<head>
<meta charset="utf-8">
<title>SkyLedgerMetrics Banner Set</title>
<link href="https://fonts.googleapis.com/css2?family=Bebas+Neue&family=Arimo:wght@400;700&display=swap" rel="stylesheet">
<style>
  :root {
    --page: #ffffff;
    --red: #d42027;
    --ink: #111111;
    --white: #ffffff;
    --sky-grey: #a9b0bd;
    --sky-tan: #c9b08a;
    --sunset-light: #f2c08c;
    --sunset-deep: #e59a5c;
    --panel-blue: #5aafe3;
    --haze-blue: #dcecf8;
  }
  * { margin: 0; padding: 0; box-sizing: border-box; }
  html, body { width: 1200px; height: 806px; overflow: hidden; background: var(--page); }
  body { position: relative; font-family: "Arimo", Arial, sans-serif; }

  .banner { position: absolute; overflow: hidden; text-align: center; }
  .banner__photo { position: absolute; inset: 0; }
  .headline { font-family: "Bebas Neue", Impact, sans-serif; font-weight: 400; letter-spacing: 0.5px; }
  .subtitle { font-weight: 700; color: var(--ink); }
  .cta { position: absolute; background: var(--red); color: var(--white); font-weight: 700; display: flex; align-items: center; justify-content: center; }

  .brand { position: absolute; display: flex; align-items: center; gap: 6px; color: var(--ink); font-weight: 700; }
  .brand__mark { background: var(--red); flex: none; }

  /* 160x600 skyscraper */
  .skyscraper { left: 124px; top: 101px; width: 160px; height: 600px; }
  .skyscraper .banner__photo { background: linear-gradient(180deg, var(--sky-grey) 0%, var(--sky-tan) 20%, #d8cdb8 45%, #b8b3aa 75%, #8b8f7c 100%); }
  .skyscraper .brand { left: 12px; top: 34px; font-size: 12px; }
  .skyscraper .brand__mark { width: 14px; height: 14px; }
  .skyscraper .headline { position: absolute; left: 0; right: 0; top: 120px; color: var(--white); font-size: 40px; line-height: 46px; }
  .skyscraper .subtitle { position: absolute; left: 0; right: 0; top: 326px; font-size: 17px; line-height: 23px; }
  .skyscraper .cta { left: 13px; top: 474px; width: 137px; height: 88px; font-size: 18px; line-height: 23px; }

  /* 300x250 medium rectangle */
  .rectangle { left: 345px; top: 102px; width: 300px; height: 250px; }
  .rectangle .banner__photo { background: radial-gradient(ellipse at 60% 55%, var(--sunset-light) 0%, var(--sunset-deep) 70%, #d88a52 100%); }
  .rectangle .brand { left: 46px; top: 16px; font-size: 20px; }
  .rectangle .brand__mark { width: 22px; height: 22px; }
  .rectangle .headline { position: absolute; left: 0; right: 0; top: 74px; color: var(--red); font-size: 40px; line-height: 35px; }
  .rectangle .subtitle { position: absolute; left: 0; right: 0; top: 147px; font-size: 16px; line-height: 20px; }
  .rectangle .cta { left: 9px; top: 202px; width: 283px; height: 37px; font-size: 16px; }

  /* 728x90 leaderboard */
  .leaderboard { left: 348px; top: 409px; width: 728px; height: 90px; }
  .leaderboard .banner__panel { position: absolute; left: 0; top: 0; width: 239px; height: 90px; background: var(--panel-blue); }
  .leaderboard .banner__photo { left: 239px; background: linear-gradient(90deg, #eef5fb 0%, var(--haze-blue) 60%, #c6dff2 100%); }
  .leaderboard .brand { left: 14px; top: 34px; font-size: 18px; }
  .leaderboard .brand__mark { width: 20px; height: 20px; }
  .leaderboard .copy { position: absolute; left: 239px; right: 0; top: 2px; }
  .leaderboard .headline { color: var(--ink); font-size: 36px; line-height: 38px; margin-left: 10px; }
  .leaderboard .subtitle { font-size: 17px; line-height: 18px; margin-left: 10px; }
  .leaderboard .cta { left: 315px; top: 57px; width: 339px; height: 26px; font-size: 17px; }
</style>
</head>
<body>

<section class="banner skyscraper">
  <div class="banner__photo" role="img" aria-label="Photo of a business jet tail seen from below against a cloudy sky"></div>
  <div class="brand"><span class="brand__mark"></span>SkyLedgerMetrics</div>
  <h1 class="headline">Calculate<br>Jet<br>Operating<br>Costs</h1>
  <p class="subtitle">Compare<br>Ownership<br>Usage<br>Scenarios</p>
  <div class="cta">COMPARE<br>OWNERSHIP<br>COSTS</div>
</section>

<section class="banner rectangle">
  <div class="banner__photo" role="img" aria-label="Photo of orange sunset clouds"></div>
  <div class="brand"><span class="brand__mark"></span>SkyLedgerMetrics</div>
  <h1 class="headline">Calculate Jet<br>Operating Costs</h1>
  <p class="subtitle">Compare Ownership<br>Usage Scenarios</p>
  <div class="cta">COMPARE OWNERSHIP COSTS</div>
</section>

<section class="banner leaderboard">
  <div class="banner__panel"></div>
  <div class="banner__photo" role="img" aria-label="Pale blue close-up photo of a jet engine intake"></div>
  <div class="brand"><span class="brand__mark"></span>SkyLedgerMetrics</div>
  <div class="copy">
    <h1 class="headline">Calculate Jet Operating Costs</h1>
    <p class="subtitle">Compare Ownership Usage Scenarios</p>
  </div>
  <div class="cta">COMPARE OWNERSHIP COSTS</div>
</section>

</body>
</html>
```